Flyer Design

Create a flyer using the logo theme. Single page for to be sent out on email. Attached is an image of the layout, below is the text. A5 and a4 versions.

Simplifying the MAZE

This short workshop is designed as a refresher for those surgeons who have attended a full Lund-MAZE training course, and wish to gain an update on the latest thinking with regards to the surgical treatment of Atrial Fibrillation.
We will start with an overview of the disease burden, talk to the foundation clinical evidence available, and cover the various lesion sets used by surgeons – with a view to simplifying the procedure. The workshop will also explain the technology used, how to treat the Left Atrial Appendage, the best ways to work with your EP colleagues, and involve a short hands-on session to familiarize you with the tools available to perform the Lund-MAZE procedure.

Faculty
{{image}}
Mr. Declan Harlow
Cardiothoracic Surgeon

Mr Harlows training was completed at the Brenhill Clinic, Rochester, Minnesota, between June 1995 and July 1997 followed by an advanced fellowship with Professor Ferris K Lomond at the Ashgrove General Hospital. Additional expertise required visits to Belgium, Italy, England and the United States. Mr Harlow now proctors internationally in order to share his knowledge and further improvement in all areas of minimal access and open cardiac and thoracic surgery.
Further overseas experience at the Ashgrove General Hospital in Canada culminated in the award of Clinical Fellowship in Cardiovascular Surgery in December 1997.

Mr Harlow has contributed to many publications and is referee for Journal articles in very highly regarded professional journals. He performs both Cardiac surgery procedures and thoracic procedures at Westmere Private Hospital and Dunmore Hospital, Melbourne. Mr Harlow has performed in excess of 200 open Maze procedures and 35 via a Thoracoscopic approach.

Venue - TBA
Time : 5pm - 7.30pm, followed by dinner and case presentations

```html
<!DOCTYPE html>
<html lang="en">
<head>
<meta charset="utf-8">
<title>Simplifying the Maze – Workshop Flyer</title>
<link href="https://fonts.googleapis.com/css2?family=Bebas+Neue&family=Crimson+Pro:wght@400;500&family=Questrial&family=Raleway:wght@200;700;800&family=Tinos:wght@400;700&display=swap" rel="stylesheet">
<style>
  :root {
    --paper: #ffffff;
    --panel-grey: #f1f1f2;
    --brand-blue: #1a84c0;
    --logo-blue: #1b72b5;
    --brand-orange: #f58220;
    --ink: #333333;
    --ink-soft: #555555;
    --label-grey: #58595b;
    --photo-dark: #1c1c1c;
    --ring-grey: #d9d9d9;
  }
  * { margin: 0; padding: 0; box-sizing: border-box; }
  html, body { width: 863px; height: 1200px; overflow: hidden; background: var(--paper); }
  .flyer { position: relative; width: 863px; height: 1200px; overflow: hidden; background: var(--paper); }

  .panel-left { position: absolute; left: 13px; top: 13px; width: 465px; height: 1173px; background: var(--panel-grey); }
  .panel-right { position: absolute; left: 478px; top: 13px; width: 372px; height: 1173px; background: var(--brand-blue); }

  .brand { position: absolute; left: 52px; top: 82px; width: 360px; text-align: center; }
  .brand-name { font-family: "Raleway", sans-serif; font-weight: 800; font-size: 62px; letter-spacing: -1px; color: var(--logo-blue); line-height: 1; }
  .brand-region { margin-top: 8px; font-family: "Raleway", sans-serif; font-weight: 700; font-size: 12.5px; letter-spacing: 0.3px; color: var(--label-grey); }

  .section-title { position: absolute; left: 53px; top: 244px; font-family: "Raleway", sans-serif; font-weight: 200; font-size: 54px; color: var(--ink-soft); letter-spacing: 1px; line-height: 1; }

  .faculty-photo { position: absolute; left: 13px; top: 298px; width: 449px; height: 340px; background: radial-gradient(ellipse at 40% 45%, #5a4a44 0%, #2a2624 40%, var(--photo-dark) 75%); }

  .title-badge { position: absolute; left: 370px; top: 257px; width: 440px; height: 430px; }
  .title-text { position: absolute; left: 400px; top: 393px; width: 388px; text-align: center; font-family: "Bebas Neue", sans-serif; font-size: 92px; line-height: 0.86; color: #fff; transform: scaleX(0.98); }

  .name-tag { position: absolute; left: 13px; top: 624px; width: 310px; height: 57px; }
  .name-tag svg { position: absolute; inset: 0; }
  .name-tag .name { position: absolute; left: 40px; top: 4px; font-family: "Crimson Pro", serif; font-weight: 500; font-size: 27px; color: #fff; line-height: 1.1; }
  .name-tag .role { position: absolute; left: 40px; top: 34px; font-family: "Crimson Pro", serif; font-size: 16.5px; color: #fff; letter-spacing: 0.3px; }

  .bio { position: absolute; left: 53px; top: 700px; width: 392px; font-family: "Tinos", serif; font-size: 12.4px; line-height: 17.4px; color: var(--ink); text-align: justify; }
  .bio p + p { margin-top: 11px; }

  .detail { position: absolute; left: 53px; width: 258px; height: 32px; display: flex; border-radius: 6px; overflow: hidden; font-family: "Tinos", serif; font-weight: 700; font-size: 24px; color: #fff; line-height: 32px; }
  .detail .label { width: 78px; background: var(--label-grey); padding-left: 6px; }
  .detail .value { flex: 1; background: var(--brand-orange); padding-left: 8px; }
  .detail-venue { top: 1049px; }
  .detail-time { top: 1086px; }
  .followup { position: absolute; left: 53px; top: 1124px; font-family: "Crimson Pro", serif; font-size: 18.5px; color: var(--ink-soft); }

  .blurb { position: absolute; left: 500px; width: 320px; text-align: center; font-family: "Questrial", sans-serif; font-size: 17.8px; line-height: 26px; color: #fff; }
  .blurb-intro { top: 58px; }
  .blurb-overview { top: 738px; }
  .blurb-hands-on { top: 921px; }
</style>
</head>
<body>
<main class="flyer">
  <div class="panel-left"></div>
  <div class="panel-right"></div>

  <header class="brand">
    <div class="brand-name">CardiaVance</div>
    <div class="brand-region">AUSTRALIA AND NEW ZEALAND</div>
  </header>

  <h2 class="section-title">FACULTY</h2>

  <div class="faculty-photo" role="img" aria-label="Portrait photograph of cardiothoracic surgeon Declan Harlow in a dark suit, arms folded, on a dark background"></div>

  <svg class="title-badge" viewBox="0 0 440 430" aria-hidden="true">
    <circle cx="217" cy="213" r="213" fill="var(--ring-grey)"/>
    <circle cx="223" cy="213" r="206" fill="var(--brand-orange)"/>
  </svg>
  <h1 class="title-text">SIMPLIFYING<br>THE MAZE</h1>

  <div class="name-tag">
    <svg viewBox="0 0 310 57" width="310" height="57" aria-hidden="true">
      <polygon points="0,0 310,0 294,57 0,57" fill="var(--brand-orange)"/>
    </svg>
    <div class="name">Mr. Declan Harlow</div>
    <div class="role">Cardiothoracic Surgeon</div>
  </div>

  <section class="bio">
    <p>Mr Harlows training was completed at the Brenhill Clinic, Rochester, Minnesota, between June 1995 and July 1997 followed by an advanced fellowship with Professor Ferris K Lomond at the Ashgrove General Hospital. Additional expertise required visits to Belgium, Italy, England and the United States. Mr Harlow now proctors internationally in order to share his knowledge and further improvement in all areas of minimal access and open cardiac and thoracic surgery.</p>
    <p>Further overseas experience at the Ashgrove General Hospital in Canada culminated in the award of Clinical Fellowship in Cardiovascular Surgery in December 1997.</p>
    <p>Mr Harlow has contributed to many publications and is referee for Journal articles in very highly regarded professional journals. He performs both Cardiac surgery procedures and thoracic procedures at Westmere Private Hospital and Dunmore Hospital, Melbourne. Mr Harlow has performed in excess of 200 open Maze procedures and 35 via a Thoracoscopic approach.</p>
  </section>

  <div class="detail detail-venue"><span class="label">Venue</span><span class="value">TBA</span></div>
  <div class="detail detail-time"><span class="label">Time</span><span class="value">5PM-7.30PM</span></div>
  <p class="followup">Followed By Dinner And Case Presentations</p>

  <p class="blurb blurb-intro">This SHORT WORKSHOP is designed as a refresher for those surgeons who have attended a full Lund-MAZE training course, and wish to gain an update on the latest thinking with regards to the surgical treatment of Atrial Fibrillation.</p>
  <p class="blurb blurb-overview">We will start with an overview of the disease burden, talk to the foundation clinical evidence available, and cover the various lesion sets used by surgeons – with a view to simplifying the procedure.</p>
  <p class="blurb blurb-hands-on">The workshop will also explain the technology used, how to treat the Left Atrial Appendage, the best ways to work with your EP colleagues, and involve a short hands-on session to familiarize you with the tools available to perform the Lund-MAZE procedure.</p>
</main>
</body>
</html>
```